Brintell's Business Card

I need some designs for a new business card including the new logo attached. An old example of our business card is also attached to show all the data that should be included on the new design.
**I added some more examples someone had mocked up**

Contact Information for Business Card

Should include all info on other examples uploaded.

```html
<!DOCTYPE html>
<html lang="en">
<head>
<meta charset="utf-8">
<title>Brintell's Business Card</title>
<link rel="stylesheet" href="https://fonts.googleapis.com/css2?family=Oswald:wght@500;700&display=swap">
<style>
  :root {
    --brand-red: #e03d35;
    --brand-blue: #2a6fb7;
    --paper: #ffffff;
    --canvas: #ffffff;
    --shadow: rgba(0, 0, 0, 0.22);
    --text-light: #ffffff;
  }
  * { box-sizing: border-box; margin: 0; padding: 0; }
  html, body {
    width: 1200px;
    height: 1200px;
    overflow: hidden;
    background: var(--canvas);
    font-family: "Oswald", "Arial Narrow", sans-serif;
  }
  .card-set {
    position: absolute;
    top: 440px;
    left: 45px;
    display: flex;
    gap: 30px;
  }
  .card {
    position: relative;
    width: 540px;
    height: 318px;
    background: var(--paper);
    box-shadow: 3px 4px 8px var(--shadow);
    overflow: hidden;
  }

  /* Front card */
  .service-band {
    position: absolute;
    top: 12px;
    left: 0;
    right: 0;
    height: 30px;
    background: var(--brand-red);
    color: var(--text-light);
    font-weight: 700;
    font-size: 19px;
    line-height: 30px;
    text-align: center;
    letter-spacing: 0.3px;
    text-transform: uppercase;
  }
  .brand-mark {
    position: absolute;
    top: 78px;
    left: 0;
    right: 0;
    display: flex;
    flex-direction: column;
    align-items: center;
    gap: 12px;
  }
  .brand-dot {
    width: 44px;
    height: 44px;
    border-radius: 50%;
    background: var(--brand-red);
  }
  .brand-name {
    font-weight: 700;
    font-size: 40px;
    line-height: 1;
    color: var(--brand-blue);
    letter-spacing: 1px;
    text-transform: uppercase;
  }
  .cta-band {
    position: absolute;
    top: 232px;
    left: 0;
    right: 0;
    height: 64px;
    background: var(--brand-blue);
    color: var(--text-light);
    font-weight: 700;
    font-size: 19px;
    line-height: 24px;
    text-align: center;
    text-transform: uppercase;
    display: flex;
    align-items: center;
    justify-content: center;
  }

  /* Back card */
  .card-back { display: flex; background: var(--paper); }
  .back-brand {
    width: 202px;
    height: 100%;
    background: var(--brand-blue);
    display: flex;
    flex-direction: column;
    align-items: center;
    justify-content: center;
    gap: 10px;
  }
  .back-brand .brand-dot {
    width: 34px;
    height: 34px;
    background: var(--text-light);
  }
  .back-brand .brand-name {
    font-size: 28px;
    color: var(--text-light);
  }
  .back-contact {
    margin-left: 4px;
    flex: 1;
    height: 100%;
    background: var(--brand-red);
    color: var(--text-light);
    padding: 100px 0 0 48px;
  }
  .person-name {
    display: inline-block;
    font-weight: 700;
    font-size: 36px;
    line-height: 1.1;
    text-transform: uppercase;
    letter-spacing: 0.5px;
    border-bottom: 2px solid var(--text-light);
    padding-bottom: 2px;
  }
  .contact-list {
    list-style: none;
    margin-top: 16px;
    font-weight: 500;
    font-size: 19px;
    line-height: 24px;
  }
  .contact-list li { display: flex; align-items: center; gap: 10px; }
  .contact-icon { width: 14px; height: 14px; fill: var(--text-light); flex: none; }
</style>
</head>
<body>
  <main class="card-set">
    <section class="card card-front">
      <div class="service-band">Serves Millbrook, IA &amp; Surrounding Areas</div>
      <div class="brand-mark">
        <span class="brand-dot"></span>
        <span class="brand-name">Brintell's</span>
      </div>
      <div class="cta-band">Call today for all your HVAC,<br>refrigeration &amp; plumbing needs.</div>
    </section>

    <section class="card card-back">
      <div class="back-brand">
        <span class="brand-dot"></span>
        <span class="brand-name">Brintell's</span>
      </div>
      <div class="back-contact">
        <h1 class="person-name">Wade Brintell</h1>
        <ul class="contact-list">
          <li>
            <svg class="contact-icon" viewBox="0 0 24 24" aria-hidden="true"><path d="M6.6 10.8a15.1 15.1 0 0 0 6.6 6.6l2.2-2.2c.3-.3.7-.4 1-.2 1.1.4 2.3.6 3.6.6.6 0 1 .4 1 1V20c0 .6-.4 1-1 1C10.6 21 3 13.4 3 4c0-.6.4-1 1-1h3.5c.6 0 1 .4 1 1 0 1.3.2 2.5.6 3.6.1.3 0 .7-.2 1z"/></svg>
            555.014.2290
          </li>
          <li>
            <svg class="contact-icon" viewBox="0 0 24 24" aria-hidden="true"><path d="M2 5h20v14H2z M4 7v.5l8 5.5 8-5.5V7l-8 5.5z" fill-rule="evenodd"/></svg>
            hvacbrintell@mailbox.com
          </li>
        </ul>
      </div>
    </section>
  </main>
</body>
</html>
```